Chocolate company needing sticker for products

I have a small chocolate company Brook Lane Sweets in Austin Texas. I make all vegan, gluten free, organic, faire trade chocolate that tastes amazing! It is allergy friendly approvable by all ages. I want to have a great sticker that i can put on our boxes and bags. I am using a lot of natural craft color and brown. I am open to color options possibly for different flavors. I want the packaging to reflect the basis of my company. It is all handmade by me but i don't want it to have to much of a crafty look to it. I have attached the logo designs I have. it the sticker can have som of the bullet points about the company that would be great. But it needs to say Locally Made in Austin Texas. it also has to have the company address.
417 West Harlow Pine Rd #238 Austin Tx 78719. These things are required by the state for food regulations. I want something that looks great and I can be really proud to put on my product! Thanks so much for all of your help in advance. Dee

I also need some other information added to the sticker. Website which is brooklanesweetsqvz.com 

Phone number 512.555.0187. Instagram brooklanesweets. Thanks for your hard work! 

Industry/Entity Type

Chocolate Company

Requirements
Must have
• The logo is added at the bottom as well as designs I like I want to have a professional look but it to be approvable by all consumers. I will gig feed back as i see what designs come through. This will probably fold out into a multi design project so i will be looking for assistance on other areas of this as well. Thanks

```html
<!DOCTYPE html>
<html lang="en">
<head>
<meta charset="utf-8">
<title>Brook Lane Sweets — Product Sticker</title>
<link rel="stylesheet" href="https://fonts.googleapis.com/css2?family=Arvo:wght@700&display=swap">
<style>
  :root {
    --tan: #e1b06e;
    --peach: #fde0cc;
    --pistachio: #f1f3c5;
    --paper: #ffffff;
  }
  * { box-sizing: border-box; margin: 0; padding: 0; }
  html, body {
    width: 1200px;
    height: 800px;
    overflow: hidden;
    background: var(--paper);
  }
  .sticker {
    position: relative;
    width: 1200px;
    height: 800px;
    background: var(--paper);
    font-family: "Arvo", "Rockwell", serif;
    color: var(--tan);
    text-transform: uppercase;
  }
  .info-strip {
    position: absolute;
    left: 0;
    width: 1200px;
    height: 50px;
    display: flex;
    align-items: center;
    font-size: 19px;
    letter-spacing: 1.6px;
    white-space: nowrap;
  }
  .info-strip--top { top: 0; padding-left: 44px; gap: 36px; }
  .info-strip--bottom { bottom: 0; padding: 0 40px 0 44px; justify-content: space-between; }
  .info-strip .label { margin-right: 16px; }

  .pattern-field {
    position: absolute;
    top: 50px;
    left: 0;
    width: 1200px;
    height: 700px;
    display: grid;
    grid-template-columns: 400px 400px 400px;
    grid-template-rows: 347px 353px;
  }
  .tile--peach { background: var(--peach); }
  .tile--pistachio { background: var(--pistachio); }

  .seal {
    position: absolute;
    left: 342px;
    top: 130px;
    width: 534px;
    height: 534px;
    border-radius: 50%;
    background: var(--tan);
    color: var(--paper);
  }
  .seal-tag {
    position: absolute;
    top: 212px;
    font-size: 22px;
    line-height: 22px;
    text-align: center;
    letter-spacing: 0.5px;
    padding: 14px 0;
    border-top: 4px solid var(--paper);
    border-bottom: 4px solid var(--paper);
  }
  .seal-tag--left { left: 27px; width: 114px; }
  .seal-tag--right { right: 27px; width: 100px; }

  .brand-name {
    position: absolute;
    left: 150px;
    top: 172px;
    width: 234px;
    text-align: center;
    font-size: 52px;
    line-height: 64px;
    letter-spacing: 1px;
  }
</style>
</head>
<body>
<main class="sticker">
  <header class="info-strip info-strip--top">
    <span>Vegan Gluten/Allergy-Free</span>
    <span><span class="label">Phone</span>512.555.0187</span>
    <span><span class="label">IG</span>brooklanesweets</span>
  </header>

  <div class="pattern-field" role="img" aria-label="White polka dot pattern on alternating peach and pale green squares">
    <div class="tile tile--peach"></div>
    <div class="tile tile--pistachio"></div>
    <div class="tile tile--peach"></div>
    <div class="tile tile--pistachio"></div>
    <div class="tile tile--peach"></div>
    <div class="tile tile--pistachio"></div>
  </div>

  <section class="seal">
    <p class="seal-tag seal-tag--left">Locally<br>Made In</p>
    <h1 class="brand-name">Brook<br>Lane<br>Sweets</h1>
    <p class="seal-tag seal-tag--right">Austin<br>Texas</p>
  </section>

  <footer class="info-strip info-strip--bottom">
    <span>417 West Harlow Pine Rd #238 Austin Tx 78719</span>
    <span>brooklanesweetsqvz.com</span>
  </footer>
</main>
</body>
</html>
```